Corvane Holdings , new business card design

investment firm with corporate clients . need double sided business card , vertical and horizontal options ,logo must be clear. prefer pantone colors only and sharp design. website also www.corvane-example.ae

Khalid Bin Rashed
Managing Director
Tel. +971 4 000 3829
Mobile +971 50 000 4172
khalid@corvane-example.ae
Palm Crest Tower, officw 18-B07, Qasr Gardens, Dubai

Contact Information for Business Card

Khalid Bin Rashed
Managing Director

Font styles to use
Serif

Colors

Designer to choose colors to be used in the design.

```html
<!DOCTYPE html>
<html lang="en">
<head>
<meta charset="utf-8">
<title>Corvane Holdings — Business Card</title>
<link rel="stylesheet" href="https://fonts.googleapis.com/css2?family=Zilla+Slab:wght@300;400&display=swap">
<style>
  :root {
    --navy: #022157;
    --steel-grey: #807e84;
    --mist: #d6d7db;
    --paper: #ffffff;
    --ink-light: #e4e6ee;
    --serif: "Zilla Slab", Georgia, serif;
  }
  * { margin: 0; padding: 0; box-sizing: border-box; }
  html, body {
    width: 1200px; height: 1200px; overflow: hidden;
    background: var(--paper);
    font-family: var(--serif);
    font-weight: 300;
  }
  .sheet { position: relative; width: 1200px; height: 1200px; }
  .card {
    position: absolute; left: 170px; width: 860px; height: 516px;
    border-radius: 24px; overflow: hidden; background: var(--mist);
  }
  .card--front { top: 50px; }
  .card--back { top: 634px; }
  .card__shapes { position: absolute; inset: 0; width: 860px; height: 516px; }
  .card__text { position: absolute; white-space: nowrap; }

  .holder-name {
    left: 0; width: 860px; top: 100px; text-align: center;
    font-size: 42px; color: var(--ink-light); line-height: 1;
  }
  .holder-rule {
    position: absolute; left: 192px; width: 466px; top: 174px; height: 2px;
    background: var(--ink-light);
  }
  .holder-title {
    left: 0; width: 860px; top: 188px; text-align: center;
    font-size: 29px; color: var(--ink-light); line-height: 1;
  }
  .contact {
    font-size: 19px; color: var(--ink-light); line-height: 1; left: 96px;
  }
  .contact--tel { top: 318px; }
  .contact--mobile { top: 369px; }
  .contact__icon { position: absolute; width: 22px; height: 24px; }
  .contact__icon--tel { left: 62px; top: 316px; }
  .contact__icon--mobile { left: 60px; top: 365px; width: 22px; height: 28px; }
  .contact--email { left: 370px; top: 364px; font-size: 24px; }
  .address {
    left: 0; width: 860px; top: 466px; text-align: center;
    font-size: 25px; color: var(--navy); font-weight: 400; line-height: 1;
  }

  .brand-name {
    left: 0; width: 860px; top: 190px; text-align: center;
    font-size: 74px; letter-spacing: 0.32em; text-indent: 0.32em;
    color: var(--navy); font-weight: 300; line-height: 1.15;
  }
  .brand-name span { display: block; font-size: 38px; letter-spacing: 0.62em; text-indent: 0.62em; }
  .website {
    left: 0; width: 860px; top: 462px; text-align: center;
    font-size: 26px; color: var(--ink-light); line-height: 1;
  }
</style>
</head>
<body>
<main class="sheet">

  <section class="card card--front" aria-label="Business card front">
    <svg class="card__shapes" viewBox="0 0 860 516" aria-hidden="true">
      <path fill="var(--navy)" d="M0,0 H860 V344 C830,400 780,429 710,429 H0 Z"/>
      <path fill="var(--steel-grey)" d="M0,429 H710 C780,429 830,400 860,344 V354 C830,410 785,437 710,437 H0 Z"/>
    </svg>
    <h1 class="card__text holder-name">Khalid Bin Rashed</h1>
    <div class="holder-rule"></div>
    <p class="card__text holder-title">Managing Director</p>

    <svg class="contact__icon contact__icon--tel" viewBox="0 0 24 24" aria-hidden="true">
      <path fill="none" stroke="var(--ink-light)" stroke-width="1.8" stroke-linejoin="round"
        d="M5 3 L9 3 L10 8 L7.5 9.5 C9 13 11 15 14.5 16.5 L16 14 L21 15 L21 19 C21 20 20 21 19 21 C10 20 4 14 3 5 C3 4 4 3 5 3 Z"/>
      <path fill="none" stroke="var(--ink-light)" stroke-width="1.6" stroke-linecap="round"
        d="M14 3.5 A7 7 0 0 1 20.5 10 M14 7 A3.5 3.5 0 0 1 17 10"/>
    </svg>
    <p class="card__text contact contact--tel">+971 4 000 3829</p>

    <svg class="contact__icon contact__icon--mobile" viewBox="0 0 22 28" aria-hidden="true">
      <rect x="3" y="1.5" width="16" height="25" rx="2.5" fill="none" stroke="var(--ink-light)" stroke-width="2"/>
      <circle cx="11" cy="22.5" r="1.4" fill="var(--ink-light)"/>
    </svg>
    <p class="card__text contact contact--mobile">+971 50 000 4172</p>

    <p class="card__text contact contact--email">khalid@corvane-example.ae</p>
    <p class="card__text address">Palm Crest Tower, officw 18-B07, Qasr Gardens, Dubai</p>
  </section>

  <section class="card card--back" aria-label="Business card back">
    <svg class="card__shapes" viewBox="0 0 860 516" aria-hidden="true">
      <path fill="var(--steel-grey)" d="M0,0 H860 V77 H170 C90,77 40,110 0,171 Z"/>
      <path fill="var(--navy)" d="M0,171 C40,110 90,77 170,77 H860 V85 H172 C95,85 45,115 0,180 Z"/>
      <path fill="var(--steel-grey)" d="M0,430 H700 C780,430 830,392 860,344 V352 C830,400 780,438 700,438 H0 Z"/>
      <path fill="var(--navy)" d="M0,438 H700 C780,438 830,400 860,352 V516 H0 Z"/>
    </svg>
    <h2 class="card__text brand-name">CORVANE<span>HOLDINGS</span></h2>
    <p class="card__text website">www.corvane-example.ae</p>
  </section>

</main>
</body>
</html>
```